Alaska Personal Injury Lawyer needs a cover for a book

We need a cover for a 90 page paperback book. We want the cover to reflect a positive result coming out of a negative situation.

More specifically, this book discusses the process for maximizing one's personal injury claim arising from automobile accidents.

We are not looking for covers that show pictures of wrecked cars, ambulances or people in wheelchairs. We prefer for the cover to show people who have gotten past their injuries and the legal process and are happy again. Much like many pharmaceutical companies do. They advertise medicines that help horrible conditions, but instead of talking or showing the horrible disease, they show the happy outcome of getting better.

The title of the book with be:
Orchard Under Quiet Hills
Untangling Your Bicycle Mishap Paperwork

I am uploading a book cover on the same topic by someone else who successfully struck a balance between a bad situation and a positive outcome.

It's up to you whether to do an entirely positive cover vs a hybrid such as the one attached. However, the design should communicate more happiness and joy than fear and worry.

Thank you!

people who have been injured in car accidents that were not their fault

Legal

Serif

• We want the cover to reflect a positive result coming out of a negative situation.
• More specifically, this book discusses the process for maximizing one's personal injury claim arising from automobile accidents.
• We prefer for the cover to show people who have gotten past their injuries and the legal process and are happy again. Much like many pharmaceutical companies do. They advertise medicines that help horrible conditions, but instead of talking or showing the horrible disease, they show the happy outcome of getting better or people enjoying life, playing with kids and family.
• It's up to you whether to do an entirely positive cover vs a hybrid such as the one attached. However, the design should communicate more happiness and joy than fear and worry.
• Since the title is "Orchard under Quiet Hills: Untangling Your Bicycle Mishap Paperwork" you might consider a nautical theme, but I encourage you to draw on your own creativity.
• We are not looking for covers that show pictures of wrecked cars, ambulances or people in wheelchairs.
• The title of the book with be:
• Orchard Under Quiet Hills
• Calmly Untangling Your Bicycle Mishap Paperwork
• I am uploading a book cover on the same topic by someone else who successfully struck a balance between a bad situation and a positive outcome.

```html
<!DOCTYPE html>
<html lang="en">
<head>
<meta charset="utf-8">
<title>Orchard Under Quiet Hills – Book Cover</title>
<link rel="stylesheet" href="https://fonts.googleapis.com/css2?family=Cinzel:wght@400;500&family=Montserrat:wght@500&family=Raleway:wght@400&display=swap">
<style>
  :root {
    --paper: #ffffff;
    --ink: #1b1b1d;
    --accent: #8a3220;
    --sky-edge: #3a4a52;
    --sky-light: #dfe4e2;
    --sun-core: #fff3d2;
    --sun-warm: #f1b25c;
    --horizon: #7f9398;
    --sea-mid: #2b727a;
    --sea-foam: #b9e4e0;
    --sea-deep: #17464e;
    --brass-light: #f2dca8;
    --brass: #b78a3c;
    --brass-dark: #6a4a1c;
  }
  * { margin: 0; padding: 0; box-sizing: border-box; }
  html, body { width: 909px; height: 1200px; overflow: hidden; background: var(--paper); }
  .cover {
    position: relative;
    width: 909px;
    height: 1200px;
    background: var(--paper);
    color: var(--ink);
  }
  .series-label {
    position: absolute;
    top: 50px; left: 0; right: 0;
    text-align: center;
    font-family: "Montserrat", sans-serif;
    font-weight: 500;
    font-size: 17px;
    letter-spacing: 0.28em;
    text-transform: uppercase;
  }
  .title {
    position: absolute;
    top: 82px; left: 0; right: 0;
    font-family: "Cinzel", serif;
    font-weight: 400;
    text-transform: uppercase;
    text-align: center;
    line-height: 1;
  }
  .title-main {
    display: block;
    height: 150px;
    font-size: 150px;
    letter-spacing: 0.005em;
  }
  .title-second {
    display: flex;
    justify-content: center;
    align-items: center;
    gap: 14px;
    height: 150px;
  }
  .title-small {
    display: flex;
    flex-direction: column;
    font-size: 38px;
    line-height: 1.05;
    text-align: left;
  }
  .compass {
    width: 122px; height: 122px;
    border-radius: 50%;
    background: radial-gradient(circle at 45% 40%, var(--brass-light) 0%, var(--brass) 55%, var(--brass-dark) 100%);
  }
  .title-large { font-size: 150px; }
  .subtitle {
    position: absolute;
    top: 398px; left: 0; right: 0;
    text-align: center;
    font-family: "Cinzel", serif;
    font-size: 23px;
    letter-spacing: 0.16em;
    text-transform: uppercase;
  }
  .subtitle .accent { color: var(--accent); }
  .hero {
    position: absolute;
    top: 446px; left: 48px;
    width: 813px; height: 612px;
    background:
      radial-gradient(ellipse 22% 18% at 50% 12%, var(--sun-core) 0%, rgba(241,178,92,0.9) 45%, rgba(241,178,92,0) 100%),
      radial-gradient(ellipse 70% 48% at 50% 22%, rgba(223,228,226,0.95) 0%, rgba(223,228,226,0) 100%),
      linear-gradient(180deg, var(--sky-edge) 0%, #8fa1a6 34%, var(--horizon) 50%, var(--sea-mid) 62%, var(--sea-foam) 76%, #4f9ca0 86%, var(--sea-deep) 100%);
  }
  .author {
    position: absolute;
    top: 1094px; left: 0; right: 0;
    text-align: center;
    font-family: "Raleway", sans-serif;
    font-size: 38px;
    letter-spacing: 0.04em;
    text-transform: uppercase;
  }
</style>
</head>
<body>
  <main class="cover">
    <p class="series-label">Alaska Personal Injury Lawyer</p>
    <h1 class="title">
      <span class="title-main">Orchard</span>
      <span class="title-second">
        <span class="title-small"><span>Under</span><span>Quiet</span></span>
        <span class="compass" role="img" aria-label="Brass compass emblem"></span>
        <span class="title-large">Hills</span>
      </span>
    </h1>
    <p class="subtitle">Untangling Your <span class="accent">Bicycle Mishap</span> Paperwork</p>
    <div class="hero" role="img" aria-label="Hopeful scene: a lighthouse shining a warm golden beacon as sunlight breaks through parting storm clouds over bright turquoise seas, with seagulls flying toward the light"></div>
    <p class="author">Author Name</p>
  </main>
</body>
</html>
```